Web Design Project

We are a SaaS company that specializes in the thrift industry POS and inventory software. We want a clean and professional site that does NOT look like a template site.

*** A little more about our business -
We offer a SaaS (Software As A Service) for a Point Of Sale and inventory control product specifically for the Thrift / Second hand industry. The software allows them to process inventory, grade/rate it, create the barcoded tags. It the does the whole retail sale process. We also offer tie-ins to Pixelyard, Chirpnest and apple/droid mobile apps to support our customers thrift stores.

We need to in incorporate the look/feel and color scheme of our logo.

I would imagine possibly a HTML5 slideshow (3-5 slides) rotating on the home page showing screenshots, etc.

I am envisioning icons representing features of our product.

PLEASE ask questions, I am sure I have left out a ton.
Updates

Requirements
Must have
• I have attached a couple of our logo's with color options. It needs to flow with that.

I have also attached a screen shot of what I think might work. This DOESN'T suggest that is what I am looking for, just a sample.

I am thinking a home page and maybe one or two sub pages
***Update, I kind of like the following concept for one of the sub-pages
http://www.quotivex.example/estimate.html

There should also be a place to highlight Pixelyard and chirpnest.

It will be a bilingual / multilingual site, so take that into account
Should not have
• I don't want it to look like a template site. It should be clean and professional.

```html
<!DOCTYPE html>
<html lang="en">
<head>
<meta charset="utf-8">
<title>brightresale – Retail Software Service</title>
<link href="https://fonts.googleapis.com/css2?family=Roboto+Condensed:wght@400;700&family=Arimo:wght@400;700&display=swap" rel="stylesheet">
<style>
:root{
  --orange:#d9541a;
  --orange-deep:#b8400f;
  --orange-light:#f08a2c;
  --heading-orange:#d9571c;
  --teal:#3a9aa8;
  --teal-dark:#2c8a99;
  --blue:#1b8fd0;
  --slate:#8a99a6;
  --text:#444;
  --muted:#777;
  --band:#e6e6e6;
  --login-bg:#dff6fa;
  --login-border:#5cb8c6;
}
*{box-sizing:border-box;margin:0;padding:0}
html,body{width:1182px;height:1200px;overflow:hidden}
body{position:relative;background:#fff;font-family:Arimo,Arial,sans-serif;color:var(--text)}
.abs{position:absolute}
.cond{font-family:"Roboto Condensed",Arial,sans-serif}

.topbar{left:0;top:0;width:1182px;height:42px;background:linear-gradient(90deg,var(--orange-deep),var(--orange) 40%,var(--orange-light) 60%,var(--orange-deep));}
.toplinks{right:28px;top:13px;display:flex;gap:24px;font:700 14px Arimo,Arial,sans-serif;color:#fff}
.toplinks span{display:flex;align-items:center;gap:6px}

.header{left:0;top:42px;width:1182px;height:99px;background:#fff}
.logo{left:48px;top:51px;display:flex;align-items:center;gap:14px}
.logo-mark{width:58px;height:58px;background:var(--blue);border-radius:4px}
.logo-name{font:700 46px "Roboto Condensed",Arial,sans-serif;color:var(--blue);letter-spacing:-0.5px}
.mainnav{top:78px;font:400 22px "Roboto Condensed",Arial,sans-serif;color:#333}

.hero{left:0;top:141px;width:1182px;height:336px;background:radial-gradient(ellipse at 28% 40%,#f5a040 0%,#e8731f 30%,#cf4e12 70%,#b8400f 100%)}
.heroband{left:0;top:477px;width:1182px;height:45px;background:#000}
.hero-title{left:31px;top:262px;font:700 37px "Roboto Condensed",Arial,sans-serif;color:#fff}
.hero-sub{left:31px;top:312px;width:540px;font:400 29px/37px "Roboto Condensed",Arial,sans-serif;color:#fff}

.slider{left:566px;top:165px;width:572px;height:320px;border:4px solid #fff;background:linear-gradient(#f3f3f3,#dcdcdc)}
.slider-art{position:absolute;left:80px;top:60px;width:300px;height:230px;background:radial-gradient(ellipse,#c9d4dc,#e4e4e4 75%);border-radius:8px}
.slider-title{position:absolute;left:280px;top:30px;font:400 28px "Roboto Condensed",Arial,sans-serif;color:var(--orange)}
.slider-reflect{left:566px;top:485px;width:572px;height:37px;background:linear-gradient(#777,#000)}
.arrow{width:36px;height:39px;background:#555;display:flex;align-items:center;justify-content:center}

.h-big{font:400 32px "Roboto Condensed",Arial,sans-serif;color:#444}
.h-orange{font:400 22px "Roboto Condensed",Arial,sans-serif;color:var(--heading-orange)}
.welcome-text{left:29px;top:597px;width:391px;font-size:12.5px;line-height:15px;text-align:justify;color:var(--muted)}
.welcome-teal{left:29px;top:695px;width:391px;font-size:13px;line-height:16px;color:var(--teal)}
.news{left:23px;width:400px;font-size:13px;line-height:16px;color:#444}
.news b{color:var(--teal);display:block}

.service-list{left:466px;top:584px;list-style:none}
.service-list li{height:31px;font-size:13px;color:var(--teal);padding-left:16px;position:relative}
.service-list li::before{content:"";position:absolute;left:2px;top:4px;border-left:6px solid var(--orange);border-top:4px solid transparent;border-bottom:4px solid transparent}

.login{left:841px;top:534px;width:322px;height:203px;background:var(--login-bg);border:1px solid var(--login-border);border-radius:7px}
.login .h-orange{position:absolute;left:18px;top:10px;font-size:25px}
.login label{position:absolute;left:19px;font-size:12.5px;color:#2e5e8a}
.login .field{position:absolute;left:93px;width:216px;height:30px;background:#fff;border:1px solid #b9dbe2;border-radius:5px}
.login .btn{position:absolute;left:220px;top:122px;width:89px;height:30px;border-radius:15px;background:linear-gradient(#f4f4f4,#d9d9d9);border:1px solid #c5c5c5;font-size:12.5px;color:#666;display:flex;align-items:center;justify-content:center}
.client-box{top:799px;width:104px;height:56px;border:1px solid #ddd;display:flex;align-items:center;justify-content:center;font:400 16px "Roboto Condensed",Arial,sans-serif;color:var(--teal)}

.lowband{left:0;top:917px;width:1182px;height:159px;background:linear-gradient(#fff,#f4f4f4 60%,#e9e9e9);border-top:1px solid #eee;border-bottom:3px solid #d3d3d3}
.divider{top:927px;height:130px;border-left:1px dotted #aaa}
.low-text{font-size:13px;line-height:15.5px;color:#444;text-align:justify}
.more{width:60px;height:20px;border-radius:10px;background:var(--teal);color:#fff;font-size:12.5px;display:flex;align-items:center;justify-content:center}

.footer{left:0;top:1079px;width:1182px;height:121px;background:var(--band)}
.footlinks{left:23px;top:1111px;font-size:13px;line-height:19.5px;color:#555}
.follow{left:1016px;top:1110px;width:136px;height:41px;border:1px solid #aaa;background:#f4f4f4;display:flex;align-items:flex-end;justify-content:center;gap:12px;padding-bottom:6px;font:700 12px Arimo,Arial,sans-serif;color:#555}
.follow small{position:absolute;left:28px;top:-4px;background:#ccc;padding:1px 5px;font-size:11px}
</style>
</head>
<body>
<div class="abs topbar"></div>
<div class="abs toplinks">
  <span><svg width="11" height="13"><path d="M1 0h6l3 3v10H1z" fill="#fff"/></svg>Company</span>
  <span><svg width="16" height="13"><ellipse cx="8" cy="6" rx="8" ry="5.5" fill="#fff"/><path d="M3 9l-1 4 5-3z" fill="#fff"/></svg>Buzz</span>
  <span><svg width="12" height="12"><circle cx="2" cy="10" r="2" fill="#fff"/><path d="M0 5a7 7 0 0 1 7 7M0 0a12 12 0 0 1 12 12" stroke="#fff" stroke-width="2" fill="none"/></svg>Blog</span>
</div>

<div class="abs header"></div>
<div class="abs logo"><div class="logo-mark"></div><div class="logo-name">brightresale</div></div>
<div class="abs mainnav" style="left:664px">Company</div>
<div class="abs mainnav" style="left:773px">Solutions</div>
<div class="abs mainnav" style="left:882px">Services</div>
<div class="abs mainnav" style="left:979px">Support</div>
<div class="abs mainnav" style="left:1076px">Supplies</div>

<div class="abs hero"></div>
<div class="abs heroband"></div>
<h1 class="abs hero-title">OUR RETAIL SOFTWARE SERVICE</h1>
<p class="abs hero-sub">High performing software and hardware for high demanding environments.</p>

<div class="abs slider-reflect"></div>
<div class="abs slider">
  <div class="slider-art" role="img" aria-label="Illustration of software feature icons bursting from an open box"></div>
  <div class="slider-title">Mobile softwaer service</div>
</div>
<div class="abs arrow" style="left:570px;top:300px"><svg width="14" height="22"><path d="M12 2L3 11l9 9" stroke="#fff" stroke-width="4" fill="none"/></svg></div>
<div class="abs arrow" style="left:1103px;top:300px;width:32px"><svg width="14" height="22"><path d="M2 2l9 9-9 9" stroke="#fff" stroke-width="4" fill="none"/></svg></div>

<h2 class="abs h-big" style="left:25px;top:537px">Welcome to our site</h2>
<p class="abs welcome-text">SaaS has become a common delivery model for most business applications, including accounting, collaboration, customer relationship management (CRM), enterprise resource planning (ERP), invoicing, human resource management (HRM), content management (CM) and service desk management.</p>
<p class="abs welcome-teal">SaaS has been incorporated into the strategy of all leading enterprise software companies.</p>

<h3 class="abs h-orange" style="left:25px;top:758px">Latest news</h3>
<div class="abs news" style="top:791px"><b>1.5.12</b>Software as service&nbsp; SaaS, typically pronounced, sometimes referred to as "on-demand software,</div>
<div class="abs news" style="top:848px"><b>1.3.12</b>Software as service&nbsp; SaaS, typically pronounced, sometimes referred to as "on-demand software,</div>

<h2 class="abs h-big" style="left:466px;top:541px;font-size:27px">Service</h2>
<ul class="abs service-list">
  <li>Software as a service&nbsp; SaaS, typically pro-</li>
  <li>nounced, sometimes referred to as "on-demand</li>
  <li>software," is a software delivery model in which</li>
  <li>software and its associated data are hosted</li>
  <li>centrally and are typically accessed by users</li>
  <li>using a thin client, normally using a web</li>
  <li>browser over the Internet.SaaS has become a</li>
  <li>common delivery model for most business</li>
  <li>applications, including accounting, collaboration,</li>
</ul>

<div class="abs login">
  <div class="h-orange">Client login</div>
  <label style="top:53px">Username:</label><div class="field" style="top:50px"></div>
  <label style="top:87px">Password:</label><div class="field" style="top:84px"></div>
  <div style="position:absolute;left:19px;top:127px;width:11px;height:11px;border:1px solid #999;background:#fff"></div>
  <label style="left:38px;top:125px">Remember Me</label>
  <div class="btn">Log In</div>
  <label style="top:155px">Forgot your password?</label>
  <label style="top:172px;color:#666">No Account Yet? <span style="color:#1f6fb0;text-decoration:underline">Create an Account now</span></label>
</div>

<h3 class="abs h-orange" style="left:849px;top:758px;font-size:26px">Client list</h3>
<div class="abs client-box" style="left:841px">Client name1</div>
<div class="abs client-box" style="left:950px">Client name2</div>
<div class="abs client-box" style="left:1060px">Client name3</div>

<div class="abs lowband"></div>
<div class="abs divider" style="left:361px"></div>
<div class="abs divider" style="left:720px"></div>
<div class="abs divider" style="left:1006px"></div>

<h3 class="abs h-orange" style="left:29px;top:930px;font-size:20px">Customer Comments</h3>
<p class="abs low-text" style="left:32px;top:962px;width:294px">Overall we are quite happy with PRM and it has validated our decision to go with it over Northvale RMS and Countertop."</p>
<div class="abs more" style="left:264px;top:1022px">more</div>

<h3 class="abs h-orange" style="left:399px;top:930px;font-size:20px">Point of Sale Information</h3>
<p class="abs low-text" style="left:396px;top:962px;width:294px">Overall we are quite happy with PRM and it has validated our decision to go with it over Northvale RMS and Countertop.Overall we are quite happy with PRM.</p>
<div class="abs more" style="left:628px;top:1022px">more</div>

<h3 class="abs h-orange" style="left:756px;top:930px;font-size:20px">Recent Press</h3>
<div class="abs news" style="left:755px;top:957px;width:240px"><b>Daily Ledger 1.2.12</b>Software as service&nbsp; SaaS, typically</div>
<div class="abs news" style="left:755px;top:996px;width:240px"><b>Daily Ledger 1.2.12</b>Software as a service&nbsp; SaaS</div>
<div class="abs more" style="left:930px;top:1024px">more</div>

<h3 class="abs h-orange" style="left:1039px;top:930px;font-size:20px">Our Software</h3>
<div class="abs" style="left:1071px;top:964px;width:22px;height:22px;border-radius:50%;background:#bbb"></div>
<div class="abs" style="left:1042px;top:1012px;font:700 14px Arimo,Arial,sans-serif;color:#aaa">Cloudcart.example</div>

<div class="abs footer"></div>
<div class="abs footlinks">SUBSCRIBER LOGIN | CONTACT US | FREE STUFF | LINKS | ARTICLES | FORUM | POS SEARCH DEMO | PRODUCTS<br>"FILL IN" COMPARISON CHART | POS CONSULTING SERVICES | POS SOFTWARE GUIDE FOR CLOTHING AND APPAREL STORES<br>&nbsp;FREE NEWSLETTER | LEGAL | PRIVACY POLICY</div>
<div class="abs follow"><small>follow us</small><span>Vidlane</span><span>Pixelyard</span></div>
</body>
</html>
```